Provide bookkeeping and accounting services to small and growing businesses

We need website and logo design using the name Dunhaven as the logo.
The target audience are small companies and startups who need:
1) Simple bookkeeping services
2) Accounting advice that only someone with many years of senior financial experience as a CPA can provide.

The services are provided by two individuals. each of whom specialize in one of the areas.

We want the website to be clean without a lot of visual distraction but don't know how to make a boring subject interesting. We believe our potential clients, small business owners, need to find what they want quickly and easily without a lot of verbiage or distractions.

We've attached a draft of the homepage and have completed the text on most of the other pages.

Target Market(s)

small and early stage growth companies in San Diego North County

Industry/Entity Type

Accounting

Number of Pages Required

1 page

Font styles to use
Sans Serif

Colors
86cfc6
33b8a4
85cae6

Requirements
Must have
• We need a design for the website homepage that includes the name Dunhaven as the logo. Must include a design for the name.
• Must have color in teal or greenish blue.
Nice to have
• White background, clean, clear, uncluttered.
• We would like to use the design in a Theme on a WordPress website. Themes Quiet Meadow and Silver Orchard are appealing to us.
Should not have
• Moving pictures

```html
<!DOCTYPE html>
<html lang="en">
<head>
<meta charset="utf-8">
<title>Dunhaven Accounting and Bookkeeping</title>
<link rel="stylesheet" href="https://fonts.googleapis.com/css2?family=Cinzel:wght@400;600&family=Lato:wght@400;700&family=Marcellus&family=Montserrat:wght@600&display=swap">
<style>
:root{
  --teal:#33b8a4;
  --teal-soft:#86cfc6;
  --teal-bar:#5ec4b4;
  --teal-dark:#1f6a5f;
  --sky:#85cae6;
  --ink:#1e1e1e;
  --text:#333;
  --muted:#666;
  --rule:#cfd6d5;
  --footer:#343434;
  --footer-deep:#262626;
  --white:#fff;
}
*{box-sizing:border-box;margin:0;padding:0}
html,body{width:743px;height:1200px;overflow:hidden;background:var(--white)}
body{position:relative;font-family:'Lato',sans-serif;color:var(--text);font-size:9px}
.abs{position:absolute}

/* header */
.brand{left:50px;top:8px;font-family:'Marcellus',serif;font-size:35px;color:var(--teal);line-height:1}
.phone{left:502px;top:13px;font-size:11.5px;font-weight:700;color:var(--ink);display:flex;align-items:center;gap:4px}
.social{display:flex;gap:7px}
.social span{width:17px;height:17px;border-radius:50%;background:var(--sky);border:1.5px solid #dfe9ec}
.social span:nth-child(1){background:#3d5a99}
.social span:nth-child(2){background:#3b86b6}
.social span:nth-child(3){background:#38a9e0}
.social span:nth-child(4){background:#d9453a}
.social.top{left:604px;top:12px}
.navbar{left:0;top:49px;width:743px;height:23px;background:var(--teal-bar)}
.tagline{left:50px;top:52px;font-family:'Marcellus',serif;font-size:13px;color:var(--ink)}
.nav{left:246px;top:49px;display:flex;height:23px}
.nav a{font-family:'Cinzel',serif;font-size:9.5px;color:var(--ink);text-decoration:none;padding:0 13px;line-height:23px;border-left:1px solid rgba(255,255,255,.35)}
.nav a:first-child{border-left:0}
.nav a.active{background:var(--teal-dark);color:var(--white)}

/* hero */
.hero{left:0;top:72px;width:743px;height:372px;background:linear-gradient(135deg,#6b5637 0%,#8d7350 35%,#3f4a58 65%,#6f7680 100%)}
.hero-text{left:0;top:160px;width:743px;text-align:center;font-family:'Montserrat',sans-serif;font-weight:600;font-size:15.5px;line-height:20px;color:var(--white);text-shadow:0 1px 3px rgba(0,0,0,.6)}

/* service cards */
.arrow{top:480px}
.card{top:398px;width:165px}
.card .frame{width:165px;height:154px;background:var(--teal);padding:9px;box-shadow:0 6px 8px -4px rgba(0,0,0,.35)}
.card .frame div{width:100%;height:100%}
.card h3{font-family:'Cinzel',serif;font-weight:600;font-size:12.5px;color:var(--ink);margin:14px 0 0 8px}
.card p{font-size:8.5px;line-height:12px;margin:6px 0 0 8px;color:var(--text)}
.card p em{font-style:normal;color:var(--teal)}

/* welcome */
.welcome{left:0;top:630px;width:743px;height:160px;background:linear-gradient(#f1f2f2,#fff)}
.section-title{font-family:'Cinzel',serif;font-size:16px;color:var(--ink)}
.section-title b{font-weight:400;color:var(--teal)}
.welcome h2{position:absolute;top:20px;width:743px;text-align:center}
.rule{height:1px;background:var(--rule)}
.rule::before{content:"";display:block;width:30%;height:2px;margin:0 auto;background:var(--teal);position:relative;top:-0.5px}
.welcome .rule{position:absolute;left:128px;top:47px;width:487px}
.welcome p{position:absolute;left:170px;top:56px;width:403px;text-align:center;font-size:8.7px;line-height:13px;color:var(--ink)}
.btn{display:inline-block;background:var(--teal);color:var(--white);font-weight:700;font-size:8.7px;padding:3px 4px;border:1px solid #2a9a89;border-radius:2px}
.welcome .btn{position:absolute;left:345px;top:124px}

/* resources + inquiry */
.resources{left:0;top:790px;width:467px;height:230px;background:linear-gradient(100deg,#e9eaea,#f7f7f7 60%,#eeeeee)}
.resources h2{position:absolute;left:49px;top:20px}
.resources .rule{position:absolute;left:49px;top:45px;width:418px}
.resources .rule::before{margin:0;width:22%}
.resources h4{position:absolute;left:49px;top:55px;font-size:9.5px;color:var(--ink)}
.ticks{position:absolute;left:49px;top:74px;width:370px;list-style:none}
.ticks li{display:flex;gap:8px;font-size:8.3px;line-height:11.5px;color:var(--ink);margin-bottom:11px}
.ticks svg{flex:none;margin-top:1px}
.resources .btn{position:absolute;left:50px;top:185px}
.inquiry{left:524px;top:790px;width:170px}
.inquiry h2{margin-top:21px}
.inquiry .rule{margin-top:7px}
.inquiry .rule::before{margin:0;width:38%}
.field{height:16px;border:1px solid #bfc6c5;border-radius:2px;margin-top:9px;font-size:7.5px;color:var(--muted);padding:2px 4px;background:var(--white)}
.field:first-of-type{margin-top:14px}
.field.msg{height:28px}
.inquiry .btn{margin-top:19px;padding:3px 13px;font-size:9.5px}

/* footer */
.footer{left:0;top:1020px;width:743px;height:148px;background:var(--footer)}
.foot-col{top:1037px}
.foot-col h5{font-family:'Cinzel',serif;font-weight:400;font-size:11px;color:#e8e8e8}
.foot-col .rule{margin-top:8px;background:#555}
.foot-col .rule::before{margin:0;width:45%;height:2px}
.links{list-style:none;margin-top:10px}
.links li{color:#ddd;font-size:8.5px;line-height:14.2px;padding-left:10px;position:relative}
.links li::before{content:"";position:absolute;left:0;top:5px;border-left:3px solid #ddd;border-top:2.5px solid transparent;border-bottom:2.5px solid transparent}
.links li.on{color:var(--teal)}
.contact{color:#ddd;font-size:8.5px;line-height:11px}
.contact .row{display:flex;gap:8px;margin-top:11px}
.contact b{color:var(--white)}
.contact .big{font-size:10.5px;font-weight:700;color:var(--white)}
.map{width:134px;height:79px;margin-top:12px;border:2px solid #999;background:linear-gradient(120deg,#bcd3e3 0%,#e8e3d3 45%,#d6d9c6 100%)}
.foot-brand{left:557px;top:1083px;width:136px;text-align:center;font-family:'Marcellus',serif;color:#5a5a5a}
.foot-brand .n{font-size:27px;line-height:1}
.foot-brand .t{font-size:10px;border-top:1px solid #555;margin-top:3px;padding-top:2px}
.bottom{left:0;top:1168px;width:743px;height:32px;background:var(--footer-deep)}
.copy{left:50px;top:1178px;font-size:8.5px;color:#ddd}
.social.bot{left:604px;top:1175px}
</style>
</head>
<body>

<header>
  <div class="abs brand">Dunhaven</div>
  <div class="abs phone">
    <svg width="10" height="12" viewBox="0 0 10 12"><path d="M2 0.5 4 3 3 4.5c.6 1.6 1.6 2.8 3 3.6L7.4 7l2.2 2.2-1.4 2.2C4.3 11 .8 7 .4 2.3Z" fill="var(--teal)"/></svg>
    012-555-0147
  </div>
  <div class="abs social top"><span></span><span></span><span></span><span></span></div>
  <div class="abs navbar"></div>
  <div class="abs tagline">Accounting and Bookkeeping</div>
  <nav class="abs nav">
    <a class="active">Home</a><a>About Us</a><a>Services</a><a>Experience</a><a>Resources</a><a>Contact Us</a>
  </nav>
</header>

<section>
  <div class="abs hero" role="img" aria-label="Overhead photo of a team working at a wooden office desk with laptops and paperwork"></div>
  <h1 class="abs hero-text">Dunhaven Offers A Flexible Range Of Accounting And Bookkeeping Services<br>And Support For Small And Growing Organizations In San Diego North County.</h1>
</section>

<section>
  <svg class="abs arrow" style="left:55px" width="8" height="14" viewBox="0 0 8 14"><path d="M7 1 1 7l6 6" fill="none" stroke="var(--teal)" stroke-width="1.5"/></svg>
  <svg class="abs arrow" style="left:680px" width="8" height="14" viewBox="0 0 8 14"><path d="M1 1l6 6-6 6" fill="none" stroke="var(--teal)" stroke-width="1.5"/></svg>

  <article class="abs card" style="left:97px">
    <div class="frame"><div role="img" aria-label="Photo of two businessmen reviewing documents at a laptop" style="background:linear-gradient(160deg,#eef2f5,#c9d2d8 60%,#9aa3a8)"></div></div>
    <h3>Bookkeeping</h3>
    <p>Lorem ipsum dolor sit amet, adipiscing consectetuer adipiscing aed <em>[...]</em></p>
  </article>
  <article class="abs card" style="left:291px">
    <div class="frame"><div role="img" aria-label="Photo of colourful financial charts with a calculator and pens" style="background:linear-gradient(150deg,#e7eef6,#9cc1df 45%,#e9c36b 75%,#7a8a99)"></div></div>
    <h3>Controller Services</h3>
    <p>Lorem ipsum dolor sit amet, adipiscing consectetuer adipiscing aed <em>[...]</em></p>
  </article>
  <article class="abs card" style="left:485px">
    <div class="frame"><div role="img" aria-label="Photo of a payroll sheet with a pen and calculator" style="background:linear-gradient(150deg,#8d9599,#d9dee2 45%,#eef1f3)"></div></div>
    <h3>Payroll</h3>
    <p>Lorem ipsum dolor sit amet, adipiscing consectetuer adipiscing aed <em>[...]</em></p>
  </article>
</section>

<section class="abs welcome">
  <h2 class="section-title">Welcome To <b>Dunhaven</b> Accounting and Bookkeeping</h2>
  <div class="rule"></div>
  <p>Dunhaven offers a flexible range of accounting and bookkeeping services and support for small and growing organizations in San Diego North County. We provide bookkeeping services specializing in LedgerPro at your offices or remotely from ours. We also provide a broad range of accounting services or financial advice.</p>
  <span class="btn">Read More</span>
</section>

<section class="abs resources">
  <h2 class="section-title">Our Resources</h2>
  <div class="rule"></div>
  <h4>Lorem ipsum dolor sit amet, consectetuer adipiscing elit</h4>
  <ul class="ticks">
    <li><svg width="10" height="10" viewBox="0 0 10 10"><rect x=".5" y="1.5" width="8" height="8" fill="none" stroke="var(--teal)"/><path d="M2 5l2 2 5-6" fill="none" stroke="var(--teal)" stroke-width="1.4"/></svg>Lorem ipsum dolor sit amet, consectetuer adipiscing elit, sed diam nonummy nibh euismod tincidunt ut laoreet dolore magna aliquam erat volutpat. Ut wisi enim ad minim veniam.</li>
    <li><svg width="10" height="10" viewBox="0 0 10 10"><rect x=".5" y="1.5" width="8" height="8" fill="none" stroke="var(--teal)"/><path d="M2 5l2 2 5-6" fill="none" stroke="var(--teal)" stroke-width="1.4"/></svg>Lorem ipsum dolor sit amet, consectetuer adipiscing elit, sed diam nonummy nibh euismod tincidunt ut laoreet dolore magna aliquam erat volutpat. Ut wisi enim ad minim veniam.</li>
    <li><svg width="10" height="10" viewBox="0 0 10 10"><rect x=".5" y="1.5" width="8" height="8" fill="none" stroke="var(--teal)"/><path d="M2 5l2 2 5-6" fill="none" stroke="var(--teal)" stroke-width="1.4"/></svg>Lorem ipsum dolor sit amet, consectetuer adipiscing elit, sed diam nonummy nibh euismod tincidunt ut laoreet dolore magna aliquam erat volutpat. Ut wisi enim ad minim veniam.</li>
  </ul>
  <span class="btn">Read More</span>
</section>

<aside class="abs inquiry">
  <h2 class="section-title">Quick <b>Inquiry</b></h2>
  <div class="rule"></div>
  <div class="field">Name:</div>
  <div class="field">Company:</div>
  <div class="field">Subject :</div>
  <div class="field msg">Message :</div>
  <span class="btn">Submit</span>
</aside>

<footer>
  <div class="abs footer"></div>
  <div class="abs foot-col" style="left:50px;width:84px">
    <h5>Quick Links</h5><div class="rule"></div>
    <ul class="links"><li class="on">Home</li><li>About Us</li><li>Services</li><li>Experience</li><li>Resources</li><li>Contact Us</li></ul>
  </div>
  <div class="abs foot-col contact" style="left:174px;width:188px">
    <h5>Contact Information</h5><div class="rule"></div>
    <div class="row"><svg width="7" height="10" viewBox="0 0 7 10"><path d="M3.5 0a3.3 3.3 0 0 1 3.3 3.3C6.8 5.8 3.5 10 3.5 10S.2 5.8.2 3.3A3.3 3.3 0 0 1 3.5 0Z" fill="var(--teal)"/><circle cx="3.5" cy="3.3" r="1.2" fill="var(--footer)"/></svg><div><b>Dunhaven Accounting and Bookkeeping</b><br>48 Harborline Way Suite 310, Seacrest,<br>CA 92000</div></div>
    <div class="row" style="margin-top:12px"><svg width="9" height="10" viewBox="0 0 10 12"><path d="M2 .5 4 3 3 4.5c.6 1.6 1.6 2.8 3 3.6L7.4 7l2.2 2.2-1.4 2.2C4.3 11 .8 7 .4 2.3Z" fill="var(--teal)"/></svg><span class="big">012-555-0147</span></div>
    <div class="row" style="margin-top:13px"><svg width="9" height="7" viewBox="0 0 9 7"><rect width="9" height="7" fill="var(--teal)"/><path d="M0 0l4.5 4L9 0" fill="none" stroke="var(--footer)"/></svg><span>info@dunhaven.com</span></div>
  </div>
  <div class="abs foot-col" style="left:387px;width:134px">
    <h5>Location Map</h5><div class="rule"></div>
    <div class="map" role="img" aria-label="Map of the office location in San Diego North County"></div>
  </div>
  <div class="abs foot-brand"><div class="n">Dunhaven</div><div class="t">Accounting and Bookkeeping</div></div>
  <div class="abs bottom"></div>
  <div class="abs copy">Copyright © 2016 Dunhaven Accounting and Bookkeeping. All Right Reserved</div>
  <div class="abs social bot"><span></span><span></span><span></span><span></span></div>
</footer>

</body>
</html>
```